Brava Helix Inc - Cutting-Edge Biotech Laboratory - Sleek & Sophisticated

Please design a website that has more of a high-tech and high-end feel, with contents outlined in the uploaded file.

Please have main tabs of the following categories: Home, About, FDA & LAWS, Science, Products, Media, Contact.

Media can include all the videos and photos.

Current website: www.bravahelixlabs.example - it needs to be much more high-end, sleek and more organized. Please do NOT follow the outlines in the old website, but follow the uploaded CONTENT file.

Target Market(s)

doctors

Industry/Entity Type

Biotechnology

Coding

Coded - Design and coding required

Number of Pages Required

5+ page

Requirements
Must have
• Logo
Nice to have
• Some lotion on the website

```html
<!DOCTYPE html>
<html lang="en">
<head>
<meta charset="utf-8">
<title>Brava Helix Inc</title>
<link rel="stylesheet" href="https://fonts.googleapis.com/css2?family=Montserrat:wght@400;500;600;700&family=Arimo:wght@400;700&display=swap">
<style>
:root{
  --gold:#b98a3a;
  --ink:#1b1b1b;
  --body:#333;
  --blue-deep:#2a1fe8;
  --blue-mid:#2f6cf0;
  --blue-light:#1fa8f5;
  --violet:#4a12e6;
  --white:#ffffff;
  --grey-bg:#eceef1;
  --field:#f1f1f1;
  --nav-pill:#ececec;
}
*{margin:0;padding:0;box-sizing:border-box}
html,body{width:1200px;height:3557px;overflow:hidden}
body{position:relative;background:var(--white);font-family:"Arimo",Arial,sans-serif;color:var(--body)}
.abs{position:absolute}
.heading-font{font-family:"Montserrat",Arial,sans-serif}

/* header */
.site-header{left:0;top:0;width:1200px;height:123px;background:var(--white)}
.brand{display:flex;align-items:center;gap:10px;font-family:"Montserrat",Arial,sans-serif;font-weight:700;font-size:22px;color:var(--gold);letter-spacing:.5px}
.brand-dot{width:26px;height:26px;border-radius:50%;background:var(--gold)}
.main-nav{display:flex;gap:0;font-family:"Montserrat",Arial,sans-serif;font-weight:600;font-size:15px;color:var(--ink);letter-spacing:.3px}
.main-nav span{padding:10px 20px;border-radius:10px}
.main-nav .active{background:var(--nav-pill);color:var(--gold)}

/* hero */
.hero{left:0;top:123px;width:1200px;height:551px;background:radial-gradient(circle at 30% 40%,#8a4cf0 0%,#4b1bc8 35%,#2a0e8e 70%,#1c0a6a 100%)}
.hero-title{right:80px;top:150px;text-align:right;color:var(--white);font-family:"Montserrat",Arial,sans-serif;font-weight:600;font-size:26px;line-height:40px;letter-spacing:.5px}
.video-thumb{left:795px;top:372px;width:325px;height:205px;border:3px solid var(--white);background:linear-gradient(135deg,#6a5ac8,#c9b28f 55%,#3a3a8a)}
.play{left:940px;top:454px;width:44px;height:44px}
.caption{left:700px;top:590px;width:420px;text-align:right;color:var(--white);font-size:14px}
.arrows{display:flex;gap:22px;color:var(--white);font-size:26px;font-weight:700}
.social-strip{left:1163px;top:173px;width:37px}
.social-strip span{display:block;width:37px;height:40px;margin-bottom:5px}

/* about */
.section-title{width:1200px;left:0;text-align:center;font-family:"Montserrat",Arial,sans-serif;font-weight:600;font-size:30px;color:var(--ink);letter-spacing:.5px}
.about-text{left:78px;top:810px;width:1044px;text-align:center;font-size:14px;line-height:29px;color:var(--body)}

/* bands */
.band-svg{left:0;top:0;width:1200px;height:3557px}

.clinical{left:78px;top:1124px;width:620px;color:var(--white)}
.clinical p{font-size:13px;font-weight:700;line-height:36px}
.clinical p strong{font-size:22px}
.clinical ul{list-style:none;margin-top:10px}
.clinical li{display:flex;align-items:center;gap:20px;font-size:17px;font-weight:700;height:44px}
.frame{border:4px solid rgba(255,255,255,.55)}
.lab-photo{left:747px;top:1110px;width:382px;height:498px;background:linear-gradient(160deg,#dfe9f2,#9fd4ee 45%,#3f9ccc 80%,#2a6aa0)}

/* team */
.team-photo-a{left:171px;top:1750px;width:386px;height:496px;background:linear-gradient(180deg,#9fb39a 0%,#6d8a5c 45%,#2c4a6e 80%,#1e3558)}
.team-photo-b{left:671px;top:1750px;width:384px;height:496px;background:linear-gradient(180deg,#d9d4cf,#c9b79e 45%,#b8a48e 80%,#9d8c7a)}
.vert-name{font-family:"Montserrat",Arial,sans-serif;font-weight:700;font-size:34px;letter-spacing:3px;writing-mode:vertical-rl}
.member-name{font-family:"Montserrat",Arial,sans-serif;font-weight:700;font-size:28px;color:var(--white);text-align:right;letter-spacing:1px}
.member-role{font-family:"Montserrat",Arial,sans-serif;font-weight:400;font-size:27px;color:var(--white);text-align:right}

/* research */
.research{left:102px;top:2490px;width:1025px;height:385px;background:linear-gradient(90deg,var(--violet),#3c18f0);color:var(--white);text-align:center}
.research h2{font-family:"Montserrat",Arial,sans-serif;font-weight:700;font-size:28px;margin-top:50px;letter-spacing:1px}
.research p{width:860px;margin:26px auto 0;font-size:16px;line-height:34px}
.btn-outline{display:inline-block;margin-top:40px;width:208px;height:52px;line-height:48px;border:2px solid var(--white);border-radius:12px;font-family:"Montserrat",Arial,sans-serif;font-weight:600;font-size:22px}

/* contact */
.contact-bg{left:0;top:2860px;width:1200px;height:520px;background:radial-gradient(circle at 20% 60%,#e4e6ea,#f7f7f8 60%)}
.info-row{display:flex;gap:32px;font-size:15px;line-height:23px;color:var(--ink)}
.info-row svg{flex:none}
.circle{width:40px;height:40px;border-radius:50%}
.field{left:655px;width:382px;height:41px;background:var(--field);font-size:14px;color:#555;padding:11px 16px;border-bottom:1px solid #fff}
.submit{left:657px;top:3309px;width:133px;height:43px;border:2px solid var(--violet);border-radius:10px;text-align:center;line-height:39px;font-family:"Montserrat",Arial,sans-serif;font-weight:700;font-size:20px;color:var(--ink);background:var(--white)}

/* footer */
.copyright{right:80px;top:3498px;font-size:13px;color:var(--body)}
</style>
</head>
<body>

<!-- diagonal colour bands -->
<svg class="abs band-svg" viewBox="0 0 1200 3557" aria-hidden="true">
  <defs>
    <linearGradient id="bandA" x1="0" y1="0" x2="1" y2="0">
      <stop offset="0" stop-color="#1fa8f5"/>
      <stop offset="0.5" stop-color="#2f6cf0"/>
      <stop offset="1" stop-color="#2a1fe8"/>
    </linearGradient>
    <linearGradient id="bandB" x1="0" y1="0" x2="1" y2="0">
      <stop offset="0" stop-color="#1fa8f5"/>
      <stop offset="0.45" stop-color="#2f6cf0"/>
      <stop offset="1" stop-color="#2a1fe8"/>
    </linearGradient>
    <linearGradient id="greyWash" x1="0" y1="0" x2="0" y2="1">
      <stop offset="0" stop-color="#ffffff"/>
      <stop offset="1" stop-color="#eceef1"/>
    </linearGradient>
  </defs>
  <rect x="0" y="1500" width="1200" height="700" fill="url(#greyWash)"/>
  <polygon points="0,1044 1200,932 1200,1518 0,1637" fill="url(#bandA)"/>
  <polygon points="0,2150 1200,1870 1200,2580 0,2710" fill="url(#bandB)"/>
</svg>

<!-- header -->
<header class="abs site-header">
  <div class="abs brand" style="left:70px;top:46px"><span class="brand-dot"></span>BRAVA HELIX</div>
  <nav class="abs main-nav" style="right:40px;top:51px">
    <span class="active">HOME</span><span>ABOUT US</span><span>FDA &amp; LAWS</span><span>SCIENCE</span><span>PRODUCTS</span><span>CONTACT</span>
  </nav>
</header>

<!-- hero -->
<section class="abs hero" role="img" aria-label="Magnified stem cells glowing in violet light"></section>
<h1 class="abs hero-title">LEADER IN REGENERATIVE MEDICINE<br>INNOVATOR OF THE INDUSTRY</h1>
<div class="abs video-thumb" role="img" aria-label="Interview video still with host Dana Whitlow"></div>
<svg class="abs play" viewBox="0 0 44 44" aria-hidden="true"><circle cx="22" cy="22" r="22" fill="#111" opacity=".8"/><polygon points="17,12 33,22 17,32" fill="#fff"/></svg>
<p class="abs caption">Interview with company owner Mateo Varga on stem cells</p>
<div class="abs arrows" style="left:578px;top:605px"><span>‹</span><span>›</span></div>
<div class="abs social-strip" aria-label="Social links">
  <span style="background:#2a1fe8"></span><span style="background:#1fa8f5"></span><span style="background:#b98a3a"></span>
</div>

<!-- about -->
<h2 class="abs section-title" style="top:734px">ABOUT US</h2>
<p class="abs about-text">Brava Helix Therapy provides Non-Embryonic Stem Cells and unique protocols to doctors in order to help their patients who face major health conditions, as well as those who simply wish to stay young and healthy. Over the past seven years of development, we have successfully conducted research into major diseases related to kidney, liver and heart failures, and have aided in helping people who have suffered stroke or brain injury to walk or talk again. We have helped to remove all traces of tumor in multiple cancer patients and have achieved notable results in fighting aging and its physical markers.</p>

<!-- clinical applications -->
<div class="abs clinical">
  <p>Brava Helix Inc is the producer and distributor of the highest quality umbilical cord, amniotic membrane &amp; placental tissue-based allograft in the industry. Our bioactive products are used for a wide variety of <strong>clinical applications including:</strong></p>
  <ul>
    <li><svg width="18" height="16" viewBox="0 0 18 16"><path d="M1 8h15M10 2l6 6-6 6" stroke="#fff" stroke-width="2.5" fill="none"/></svg>Orthopedics</li>
    <li><svg width="18" height="16" viewBox="0 0 18 16"><path d="M1 8h15M10 2l6 6-6 6" stroke="#fff" stroke-width="2.5" fill="none"/></svg>Sports Medicine</li>
    <li><svg width="18" height="16" viewBox="0 0 18 16"><path d="M1 8h15M10 2l6 6-6 6" stroke="#fff" stroke-width="2.5" fill="none"/></svg>Wound Care</li>
    <li><svg width="18" height="16" viewBox="0 0 18 16"><path d="M1 8h15M10 2l6 6-6 6" stroke="#fff" stroke-width="2.5" fill="none"/></svg>Podiatry</li>
    <li><svg width="18" height="16" viewBox="0 0 18 16"><path d="M1 8h15M10 2l6 6-6 6" stroke="#fff" stroke-width="2.5" fill="none"/></svg>Pain Management</li>
  </ul>
</div>
<div class="abs frame" style="left:714px;top:1084px;width:384px;height:500px"></div>
<div class="abs lab-photo" role="img" aria-label="Scientist holding a petri dish beside a molecule model"></div>

<!-- team -->
<h2 class="abs section-title" style="top:1664px">OUR TEAM</h2>
<div class="abs team-photo-a" role="img" aria-label="Portrait of Mateo Varga outdoors on a campus lawn"></div>
<div class="abs frame" style="left:147px;top:1784px;width:380px;height:434px;border-color:rgba(255,255,255,.7)"></div>
<div class="abs vert-name" style="left:190px;top:1810px;color:rgba(255,255,255,.45)">MATEO VARGA</div>
<div class="abs team-photo-b" role="img" aria-label="Portrait of Lena Ostrow"></div>
<div class="abs frame" style="left:645px;top:1750px;width:345px;height:468px;border-color:rgba(255,255,255,.7)"></div>
<div class="abs vert-name" style="left:695px;top:1860px;color:rgba(90,90,90,.55)">LENA OSTROW</div>
<div class="abs member-name" style="left:171px;top:2268px;width:386px">MATEO VARGA</div>
<div class="abs member-role" style="left:171px;top:2308px;width:386px">Chief Scientist</div>
<div class="abs member-name" style="left:600px;top:2268px;width:460px">LENA OSTROW</div>
<div class="abs member-role" style="left:600px;top:2308px;width:460px">Stem Cell Project Manager</div>
<div class="abs arrows" style="left:578px;top:2386px"><span>‹</span><span>›</span></div>

<!-- research -->
<div class="abs contact-bg" role="img" aria-label="Faint grey cell texture"></div>
<section class="abs research">
  <h2>RESEARCH</h2>
  <p>Brava Helix Inc in keenly interested in stem cell research, in areas of both laboratory and clinical studies. We strive to in understand the multitude of uses of stem cells and the ideal parameters of such usage. Contact us about possible research partnerships.</p>
  <span class="btn-outline">Contact Us</span>
</section>
<div class="abs frame" style="left:78px;top:2460px;width:1020px;height:386px;border-color:rgba(255,255,255,.45)"></div>

<!-- contact -->
<h2 class="abs section-title" style="top:2959px">CONTACT US</h2>
<div class="abs info-row" style="left:163px;top:3064px">
  <svg width="22" height="28" viewBox="0 0 22 28"><path d="M11 1a9 9 0 0 0-9 9c0 7 9 17 9 17s9-10 9-17a9 9 0 0 0-9-9z" fill="#111"/><circle cx="11" cy="10" r="3.5" fill="#fff"/></svg>
  <span>1280 Alder Crest Drive,<br>Fairmont Ridge,<br>MI, 48000</span>
</div>
<div class="abs info-row" style="left:163px;top:3170px">
  <svg width="24" height="20" viewBox="0 0 24 20"><rect x="1.5" y="2" width="21" height="16" rx="2" fill="none" stroke="#111" stroke-width="2"/><path d="M2 4l10 8 10-8" fill="none" stroke="#111" stroke-width="2"/></svg>
  <span>info@bravahelixinc.example</span>
</div>
<div class="abs info-row" style="left:165px;top:3232px">
  <svg width="18" height="26" viewBox="0 0 18 26"><rect x="1.5" y="1.5" width="15" height="23" rx="3" fill="none" stroke="#111" stroke-width="2.5"/><circle cx="9" cy="20" r="1.5" fill="#111"/></svg>
  <span style="margin-left:5px">Mateo Varga Jr : (555) 201-4470<br><span style="display:inline-block;margin-top:12px">Lena Ostrow &nbsp;&nbsp;&nbsp;&nbsp;: (555) 318-6625</span></span>
</div>
<div class="abs" style="left:165px;top:3313px;display:flex;gap:6px" aria-label="Social links">
  <span class="circle" style="background:#1a2a8a"></span>
  <span class="circle" style="background:#1fa8f5"></span>
  <span class="circle" style="background:#b98a3a"></span>
  <span class="circle" style="background:#2a1fe8"></span>
</div>

<div class="abs field" style="top:3038px">Name</div>
<div class="abs field" style="top:3094px">Email</div>
<div class="abs field" style="top:3150px">Subject</div>
<div class="abs field" style="top:3207px;height:81px">Message</div>
<div class="abs submit">Submit</div>

<!-- footer -->
<footer>
  <div class="abs brand" style="left:70px;top:3428px"><span class="brand-dot"></span>BRAVA HELIX</div>
  <nav class="abs main-nav" style="right:40px;top:3443px;font-size:14px">
    <span style="color:var(--gold)">HOME</span><span>ABOUT US</span><span>FDA &amp; LAWS</span><span>SCIENCE</span><span>PRODUCTS</span><span>CONTACT</span>
  </nav>
  <p class="abs copyright">© 2018 &nbsp;|&nbsp; www.bravahelixlabs.example</p>
</footer>

</body>
</html>
```